"The Wandering Mentor", a Higher Ed blogger, would like a wordpress design

I would like a wordpress design for blogs written by "The Wandering Mentor." that can be easily expanded by me once the initial design is complete.

Here is context which I would like included on the Home/Welcome page: "I started The Wandering Mentor in 2021 to write about the practice of academic advising through the lens of horsemanship. After one year of developing skills as a brand new equestrian, I couldn’t help but notice the similarities between my vocation as an academic advisor and my avocation as a budding equestrian. I hope my musings about my journey in two very different fields will cultivate curiosity, widen your aperture and ignite academic advisors to take their practice to the next level. "

The wordpress will primarily have blogs by myself or guest bloggers writing about academic advising for advisors, but I may widen my audience to include students and families. I'd like to have readers submit questions that I can answer. Depending on interest, I may want to have a section on Horsemanship but that is not truly the focus of this site.

I'd like the feel of the site to be positive, fresh, modern (but not too wild), with the emphasis on Higher Ed/Academic Advising as opposed to equestrian pursuits. I don't want it to feel clunky and blocky like some sites that have to do with education. I'm hoping that readers will have some "aha" moments after reading some of the posts.

I have included my logo files

```html
<!DOCTYPE html>
<html lang="en">
<head>
<meta charset="utf-8">
<title>The Wandering Mentor</title>
<link rel="stylesheet" href="https://fonts.googleapis.com/css2?family=Montserrat:wght@300;400;500;600;700;800&display=swap">
<style>
:root{
  --gold:#d6ad6b;
  --black:#000;
  --ink:#fff;
  --muted:#cfcfcf;
  --field:#161616;
  --line:#2a2a2a;
  --footer:#1b1b1b;
  --bar:#0b0b0b;
}
*{box-sizing:border-box;margin:0;padding:0}
html,body{width:1200px;height:3131px;overflow:hidden;background:var(--black)}
body{position:relative;font-family:"Montserrat",sans-serif;color:var(--ink)}
.abs{position:absolute}

/* hero */
.hero{position:absolute;left:0;top:0;width:1200px;height:600px;overflow:hidden}
.hero-photo{position:absolute;inset:0;background:linear-gradient(100deg,#8d8578 0%,#5b534a 35%,#3b342d 60%,#2a241f 100%)}
.hero-shade{position:absolute;inset:0;background:radial-gradient(ellipse at 50% 45%,rgba(0,0,0,.05),rgba(0,0,0,.45))}
.hero-curve{position:absolute;left:0;top:0}
.brand{position:absolute;left:0;width:1200px;top:16px;text-align:center}
.brand-dot{width:70px;height:70px;border:2px solid var(--gold);border-radius:50%;margin:0 auto 10px}
.brand-name{font-size:21px;font-weight:400;color:var(--ink)}
.menu-btn{position:absolute;left:997px;top:24px;width:42px;height:42px;border-radius:50%;background:#000;border:2px solid #fff;display:flex;flex-direction:column;align-items:center;justify-content:center;gap:4px}
.menu-btn span{display:block;width:18px;height:2px;background:var(--gold)}
.hero-title{position:absolute;left:0;width:1200px;top:292px;text-align:center;font-weight:800;font-size:46px;line-height:52px;letter-spacing:.5px}
.hero-sub{position:absolute;left:0;width:1200px;top:402px;text-align:center;font-weight:600;font-size:22px}

/* posts */
.post-img{position:absolute;background:linear-gradient(160deg,#4e5a44,#8a8a7e 55%,#6d5a45)}
.badge{position:absolute;background:var(--gold);color:#fff;font-size:13px;padding:5px 9px;line-height:16px}
.post-title{position:absolute;font-weight:500;font-size:23px;line-height:32px}
.post-title.small{font-size:13.5px;line-height:20px}
.excerpt{position:absolute;font-size:13.5px;line-height:24.5px;color:var(--muted)}
.excerpt.small{font-size:12px;line-height:22px}
.more{position:absolute;color:var(--gold);text-decoration:underline;font-weight:600;font-size:16.5px}
.more.small{font-size:13px}
.divider{position:absolute;left:160px;width:560px;height:1px;background:var(--line)}
.load-more{position:absolute;left:160px;top:2282px;width:143px;height:45px;background:var(--gold);color:#fff;font-weight:600;font-size:15px;display:flex;align-items:center;justify-content:center}

/* sidebar */
.side-head{position:absolute;left:776px;font-size:20px;font-weight:500}
.side-rule{position:absolute;left:776px;width:263px;height:2px;background:var(--gold);opacity:.75}
.field{position:absolute;left:776px;width:263px;background:var(--field);border:1px solid #222;color:#ddd;font-size:11.5px;padding:0 10px;display:flex;align-items:center}
.search-btn{position:absolute;left:990px;top:701px;width:49px;height:42px;background:var(--gold);display:flex;align-items:center;justify-content:center}
.popular{position:absolute;left:776px;width:263px;display:flex;gap:13px;padding-bottom:10px;border-bottom:1px solid var(--line)}
.popular-thumb{width:63px;height:52px;flex:none;background:linear-gradient(135deg,#6b5a48,#9a8d7c 60%,#3e4a52)}
.popular-title{font-size:13px;line-height:19px}
.popular-date{font-size:11px;color:var(--gold);font-weight:600}
.gold-btn{position:absolute;left:776px;width:263px;background:var(--gold);color:#fff;font-weight:600;display:flex;align-items:center;justify-content:center}
.cat{position:absolute;left:776px;font-size:13.5px;display:flex;align-items:center;gap:8px}
.tags{position:absolute;left:776px;top:1686px;width:263px;display:flex;flex-direction:column;gap:9px}
.tag-row{display:flex;gap:7px}
.tag{background:#151515;border:1px solid #2a2a2a;font-size:11px;height:26px;display:flex;align-items:center;justify-content:center;padding:0 6px;white-space:nowrap}
.social{position:absolute;left:776px;display:flex;align-items:center;gap:8px;font-size:12.5px}
.social-dot{width:31px;height:31px;border-radius:50%}
.social a{font-weight:600;text-decoration:underline}

/* about */
.about-ring{position:absolute;left:167px;top:2424px;width:334px;height:334px;border-radius:50%;border:1.5px solid var(--gold)}
.about-photo{position:absolute;left:179px;top:2436px;width:310px;height:310px;border-radius:50%;background:radial-gradient(circle at 50% 40%,#7a8a62,#3c5a34 55%,#5b3b22)}
.about-title{position:absolute;left:537px;top:2462px;font-size:39px;font-weight:300;letter-spacing:.5px}
.about-text{position:absolute;left:537px;top:2514px;width:475px;font-size:13.5px;line-height:24.5px;color:var(--muted);letter-spacing:.3px}
.about-text p+p{margin-top:6px}

/* footer */
.footer{position:absolute;left:0;top:2820px;width:1200px;height:311px;background:var(--footer)}
.footer-curve{position:absolute;left:0;top:2820px}
.footer-mark{position:absolute;left:535px;top:2855px;width:130px;height:130px;border-radius:50%;background:#111;border:3px solid #000;display:flex;align-items:center;justify-content:center;text-align:center;font-size:12px;font-weight:600;color:var(--gold);line-height:16px}
.footer-nav{position:absolute;left:0;width:1200px;top:3027px;text-align:center;font-size:14px;color:#e5e5e5}
.footer-nav span{margin:0 7px}
.bottom-bar{position:absolute;left:0;top:3087px;width:1200px;height:44px;background:var(--bar);font-size:13.5px;color:#ddd}
.bottom-bar .copy{position:absolute;left:163px;top:14px}
.bottom-bar .legal{position:absolute;right:162px;top:14px}
.bottom-bar .legal span{margin:0 12px}
</style>
</head>
<body>

<header class="hero">
  <div class="hero-photo" role="img" aria-label="Photo of an advisor meeting with a student across a desk"></div>
  <div class="hero-shade"></div>
  <svg class="hero-curve" width="1200" height="600" viewBox="0 0 1200 600"><path d="M0 505 Q600 680 1200 505 L1200 600 L0 600 Z" fill="#000"/></svg>
  <div class="brand"><div class="brand-dot"></div><div class="brand-name">The Wandering Mentor</div></div>
  <div class="menu-btn"><span></span><span></span><span></span></div>
  <h1 class="hero-title">THE WANDERING<br>MENTOR</h1>
  <p class="hero-sub">Your Partner in Higher Education</p>
</header>

<!-- post 1 -->
<div class="post-img" style="left:161px;top:669px;width:559px;height:286px" role="img" aria-label="Rider jumping a horse over a fence"></div>
<div class="badge" style="left:617px;top:678px">13 Sep 2021</div>
<h2 class="post-title" style="left:160px;top:974px;width:565px">Lorem Ipsum Is Simply Dummy Text Of Printing And Typesetting Industry</h2>
<p class="excerpt" style="left:160px;top:1048px;width:565px">Lorem Ipsum is simply dummy text of the printing and typesetting industry. Lorem Ipsum has been the industry's standard dummy text ever since the 1500s, when an unknown printer took a galley of type and scrambled</p>
<a class="more" style="left:161px;top:1137px">Continue Reading</a>
<div class="divider" style="top:1203px"></div>

<!-- posts 2 & 3 -->
<div class="post-img" style="left:161px;top:1249px;width:263px;height:207px;background:linear-gradient(135deg,#e9e4df,#b8a697 60%,#6d4a34)" role="img" aria-label="Two women working on a laptop"></div>
<div class="badge" style="left:324px;top:1260px">13 Sep 2021</div>
<h3 class="post-title small" style="left:162px;top:1480px;width:268px">Lorem Ipsum Is Simply Dummy Text Of Printing And Typesetting...</h3>
<p class="excerpt small" style="left:161px;top:1523px;width:268px">Lorem Ipsum is simply dummy text of the printing and typesetting industry...</p>
<a class="more small" style="left:161px;top:1580px">Continue Reading</a>

<div class="post-img" style="left:458px;top:1249px;width:263px;height:207px;background:linear-gradient(135deg,#3c5a3a,#8b6a4a 55%,#3a3a3a)" role="img" aria-label="Students studying together at an outdoor table"></div>
<div class="badge" style="left:621px;top:1260px">13 Sep 2021</div>
<h3 class="post-title small" style="left:459px;top:1480px;width:268px">Lorem Ipsum Is Simply Dummy Text Of Printing And Typesetting...</h3>
<p class="excerpt small" style="left:458px;top:1523px;width:268px">Lorem Ipsum is simply dummy text of the printing and typesetting industry...</p>
<a class="more small" style="left:458px;top:1580px">Continue Reading</a>
<div class="divider" style="top:1641px"></div>

<!-- post 4 -->
<div class="badge" style="left:160px;top:1690px">13 Sep 2021</div>
<h2 class="post-title" style="left:160px;top:1733px;width:565px">Lorem Ipsum Is Simply Dummy Text Of Printing And Typesetting Industry</h2>
<p class="excerpt" style="left:160px;top:1807px;width:565px">Lorem Ipsum is simply dummy text of the printing and typesetting industry. Lorem Ipsum has been the industry's standard dummy text ever since the 1500s, when an unknown printer took a galley of type and scrambled</p>
<a class="more" style="left:161px;top:1896px">Continue Reading</a>
<div class="divider" style="top:1962px"></div>

<!-- post 5 -->
<div class="post-img" style="left:161px;top:2008px;width:263px;height:207px;background:linear-gradient(135deg,#c9c2b4,#7a6a5a 50%,#2f3f5a)" role="img" aria-label="Two students smiling in an office"></div>
<div class="badge" style="left:456px;top:2025px">13 Sep 2021</div>
<h3 class="post-title small" style="left:456px;top:2065px;width:268px">Lorem Ipsum Is Simply Dummy Text Of Printing And Typesetting...</h3>
<p class="excerpt small" style="left:456px;top:2108px;width:268px">Lorem Ipsum is simply dummy text of the printing and typesetting industry...</p>
<a class="more small" style="left:456px;top:2165px">Continue Reading</a>

<div class="load-more">Load More</div>

<!-- sidebar -->
<h4 class="side-head" style="top:664px">Search For Blog</h4>
<div class="field" style="top:701px;height:42px;font-style:italic;font-size:13px">Search</div>
<div class="search-btn"><svg width="20" height="20" viewBox="0 0 20 20" fill="none" stroke="#fff" stroke-width="2"><circle cx="8" cy="8" r="6"/><path d="M12.5 12.5 18 18"/></svg></div>
<div class="side-rule" style="top:773px"></div>

<h4 class="side-head" style="top:799px">Popular Posts</h4>
<div class="popular" style="top:837px"><div class="popular-thumb" role="img" aria-label="Students in a classroom"></div><div><div class="popular-title">Lorem Ipsum tex printing and typesetting...</div><div class="popular-date">13 Sep 2021</div></div></div>
<div class="popular" style="top:919px"><div class="popular-thumb" role="img" aria-label="Rider with a horse"></div><div><div class="popular-title">Lorem Ipsum tex printing and typesetting...</div><div class="popular-date">13 Sep 2021</div></div></div>
<div class="popular" style="top:1001px"><div class="popular-thumb" role="img" aria-label="Advisor meeting"></div><div><div class="popular-title">Lorem Ipsum tex printing and typesetting...</div><div class="popular-date">13 Sep 2021</div></div></div>
<div class="popular" style="top:1082px;border-bottom:none"><div class="popular-thumb" role="img" aria-label="Group study session"></div><div><div class="popular-title">Lorem Ipsum tex printing and typesetting...</div><div class="popular-date">13 Sep 2021</div></div></div>
<div class="side-rule" style="top:1163px"></div>

<h4 class="side-head" style="top:1193px">Readers Submit Questions</h4>
<div class="field" style="top:1229px;height:37px">Email Address</div>
<div class="field" style="top:1274px;height:52px;align-items:flex-start;padding-top:10px">Submit&nbsp; Your Questions</div>
<div class="gold-btn" style="top:1342px;height:37px;font-size:19px">Post Question</div>

<h4 class="side-head" style="top:1404px">Categories</h4>
<div class="cat" style="top:1443px"><svg width="11" height="10" viewBox="0 0 11 10" fill="none" stroke="#d6ad6b" stroke-width="1.6"><path d="M1 1l4 4-4 4M6 1l4 4-4 4"/></svg>Education</div>
<div class="cat" style="top:1474px"><svg width="11" height="10" viewBox="0 0 11 10" fill="none" stroke="#d6ad6b" stroke-width="1.6"><path d="M1 1l4 4-4 4M6 1l4 4-4 4"/></svg>Academic</div>
<div class="cat" style="top:1505px"><svg width="11" height="10" viewBox="0 0 11 10" fill="none" stroke="#d6ad6b" stroke-width="1.6"><path d="M1 1l4 4-4 4M6 1l4 4-4 4"/></svg>Consulting</div>
<div class="cat" style="top:1536px"><svg width="11" height="10" viewBox="0 0 11 10" fill="none" stroke="#d6ad6b" stroke-width="1.6"><path d="M1 1l4 4-4 4M6 1l4 4-4 4"/></svg>Advisor</div>
<div class="cat" style="top:1567px"><svg width="11" height="10" viewBox="0 0 11 10" fill="none" stroke="#d6ad6b" stroke-width="1.6"><path d="M1 1l4 4-4 4M6 1l4 4-4 4"/></svg>Business</div>
<div class="side-rule" style="top:1615px"></div>

<h4 class="side-head" style="top:1644px">Tags</h4>
<div class="tags">
  <div class="tag-row"><span class="tag" style="width:81px">Education</span><span class="tag" style="width:84px">Academic</span><span class="tag" style="width:91px">Consulting</span></div>
  <div class="tag-row"><span class="tag" style="width:104px">Lorem Ipsum</span><span class="tag" style="width:60px">Advisor</span><span class="tag" style="width:76px">Business</span></div>
  <div class="tag-row"><span class="tag" style="width:81px">Education</span><span class="tag" style="width:84px">Academic</span><span class="tag" style="width:91px">Consulting</span></div>
  <div class="tag-row"><span class="tag" style="width:104px">Lorem Ipsum</span><span class="tag" style="width:60px">Advisor</span><span class="tag" style="width:76px">Business</span></div>
</div>
<div class="side-rule" style="top:1848px"></div>

<h4 class="side-head" style="top:1876px;left:778px">Social Connect</h4>
<div class="social" style="top:1919px"><span class="social-dot" style="background:#3b5a98"></span>Follow us on <a style="color:#6c86c4">Friendbook</a></div>
<div class="social" style="top:1960px"><span class="social-dot" style="background:#2aa3e6"></span>Follow us on <a style="color:#3fb0ec">Chirper</a></div>
<div class="social" style="top:2001px"><span class="social-dot" style="background:#e4241f"></span>Subscribe <a style="color:#e8342c">Tubecast</a></div>
<div class="social" style="top:2044px"><span class="social-dot" style="background:#b83290"></span>Follow us on <a style="color:#c0489a">Snapgram</a></div>
<div class="side-rule" style="top:2103px"></div>

<h4 class="side-head" style="top:2133px;left:778px">Join Our Newsletter</h4>
<p class="abs" style="left:776px;top:2170px;width:263px;font-size:13px;line-height:21px;color:var(--muted)">Lorem Ipsum is simply text of the printing and typesetting.</p>
<div class="field" style="top:2229px;height:41px;font-size:13px;gap:8px"><svg width="14" height="11" viewBox="0 0 14 11" fill="none" stroke="#d6ad6b" stroke-width="1.3"><rect x=".7" y=".7" width="12.6" height="9.6"/><path d="M.7 .7 7 6l6.3-5.3"/></svg>Enter Your Email</div>
<div class="gold-btn" style="top:2282px;height:40px;font-size:15px;left:778px;width:261px">Subscribe</div>

<!-- about -->
<div class="about-ring"></div>
<div class="about-photo" role="img" aria-label="Rider on a chestnut horse in a green paddock"></div>
<h2 class="about-title">The Wandering Mentor</h2>
<div class="about-text">
  <p>We started The Wandering Mentor in 2021 to write about the practice of academic advising through the lens of horsemanship. After one year of developing skills as a brand new equestrian, we couldn’t help but notice the similarities between our vocation as an academic advisor and my avocation as a budding equestrian.</p>
  <p>We hope our musings about our journey in two very different fields will cultivate curiosity, widen your aperture and ignite academic advisors to take their practice to the next level.</p>
</div>

<!-- footer -->
<footer>
  <div class="footer"></div>
  <svg class="footer-curve" width="1200" height="80" viewBox="0 0 1200 80"><path d="M0 0 H1200 V8 Q600 130 0 8 Z" fill="#000"/></svg>
  <div class="footer-mark">The Wandering<br>Mentor</div>
  <nav class="footer-nav">Home <span>|</span> Posts&nbsp; Advisor Spotlight <span>|</span> About Wandering Mentor <span>|</span> Advisor Tips <span>|</span> Contact</nav>
  <div class="bottom-bar">
    <div class="copy">Copyright © 2021 <b>The Wandering Mentor</b>. All Rights Reserved.</div>
    <div class="legal">Privacy Policy<span>|</span>Disclaimer</div>
  </div>
</footer>

</body>
</html>
```